Child Care Centre needs new roadside billboard / sign*

We have a 2400mm x 1200mm sign that needs to be refreshed. The design is dated and we want to create a new cleaner, more readable roadside signIt needs to be readable from about 100m awayThe text requirements are simple, but we need it to have a warm, family feel.We are located in a small beach side community and we have a lot of bright colours in our centre (a lot of blues and yellows)https://www.maplegrovechildcare.com.au/

Target Market(s)

Parents of young children

Industry/Entity Type

Childcare

Colors
fbed22
0355a3

Requirements
Must have
• Readable from c.100m
• Simple, warm design
Should not have
• Cluttered or overly busy

```html
<!DOCTYPE html>
<html lang="en">
<head>
<meta charset="utf-8">
<title>Maple Grove Early Education – Roadside Sign</title>
<link rel="stylesheet" href="https://fonts.googleapis.com/css2?family=Archivo:wght@800&family=Archivo+Black&display=swap">
<style>
  :root {
    --navy: #2b2a72;
    --sky: #00aeef;
    --sign-blue: #0355a3;
    --band-blue: #0a5896;
    --divider-blue: #1d56a8;
    --sunshine: #fbed22;
    --ink: #111111;
    --text-dark: #231f20;
    --paper: #ffffff;
    --arrow-shadow: #3a3a3a;
  }
  html, body {
    margin: 0;
    padding: 0;
    width: 1200px;
    height: 600px;
    overflow: hidden;
    background: var(--paper);
  }
  .billboard {
    display: block;
    width: 1200px;
    height: 600px;
  }
  .headline {
    font-family: "Archivo Black", "Arial Black", sans-serif;
    paint-order: stroke fill;
    stroke: var(--ink);
    stroke-linejoin: round;
  }
  .headline--white { fill: var(--paper); stroke-width: 5; }
  .headline--yellow { fill: var(--sunshine); stroke-width: 7; }
  .headline--phone { fill: var(--sunshine); stroke-width: 6; }
  .brand-name {
    font-family: "Archivo Black", "Arial Black", sans-serif;
    fill: var(--navy);
  }
  .service {
    font-family: "Archivo", "Arial", sans-serif;
    font-weight: 800;
    fill: var(--text-dark);
  }
  .service-divider { stroke: var(--divider-blue); stroke-width: 3; }
</style>
</head>
<body>
<svg class="billboard" viewBox="0 0 1200 600" xmlns="http://www.w3.org/2000/svg" role="img" aria-label="Maple Grove Early Education: open 52 weeks a year, 6.30am to 6.30pm">
  <defs>
    <linearGradient id="sky-band" x1="0" y1="0" x2="0" y2="1">
      <stop offset="0" stop-color="var(--navy)"/>
      <stop offset="0.12" stop-color="var(--navy)"/>
      <stop offset="0.48" stop-color="var(--sky)"/>
      <stop offset="0.88" stop-color="var(--navy)"/>
      <stop offset="1" stop-color="var(--sign-blue)"/>
    </linearGradient>
  </defs>

  <!-- Hours band -->
  <rect class="hours-band" x="0" y="0" width="1200" height="352" fill="url(#sky-band)"/>

  <!-- Brand arrow -->
  <g class="brand-arrow">
    <polygon points="0,46 497,46 607,167 497,287 0,287" fill="var(--arrow-shadow)"/>
    <polygon points="-5,42 484,42 598,165 484,285 -5,285" fill="var(--paper)" stroke="var(--ink)" stroke-width="5" stroke-linejoin="miter"/>
  </g>

  <!-- Brand name -->
  <g class="brand">
    <circle cx="62" cy="170" r="34" fill="var(--sunshine)"/>
    <text class="brand-name" x="112" y="160" font-size="54" textLength="388" lengthAdjust="spacingAndGlyphs">Maple Grove</text>
    <text class="brand-name" x="146" y="214" font-size="40" textLength="368" lengthAdjust="spacingAndGlyphs">Early Education</text>
  </g>

  <!-- Headlines -->
  <text class="headline headline--white" x="651" y="72" font-size="52" textLength="506" lengthAdjust="spacingAndGlyphs">52 WEEKS A YEAR</text>
  <text class="headline headline--yellow" x="632" y="236" font-size="178" textLength="530" lengthAdjust="spacingAndGlyphs">OPEN</text>
  <text class="headline headline--white" x="624" y="316" font-size="64" textLength="532" lengthAdjust="spacingAndGlyphs">6.30<tspan font-size="44">AM</tspan> – 6.30<tspan font-size="44">PM</tspan></text>

  <!-- Services band -->
  <rect class="services-band" x="0" y="352" width="1200" height="132" fill="var(--paper)"/>
  <line class="service-divider" x1="441" y1="365" x2="441" y2="471"/>
  <line class="service-divider" x1="851" y1="365" x2="851" y2="471"/>

  <text class="service" x="20" y="409" font-size="38" textLength="383" lengthAdjust="spacingAndGlyphs">6 WEEKS <tspan font-size="28">TO</tspan> 6 YEARS</text>
  <text class="service" x="52" y="454" font-size="38" textLength="330" lengthAdjust="spacingAndGlyphs">(LONG DAY CARE)</text>

  <text class="service" x="461" y="409" font-size="38" textLength="367" lengthAdjust="spacingAndGlyphs">BEFORE AND AFTER</text>
  <text class="service" x="516" y="454" font-size="38" textLength="268" lengthAdjust="spacingAndGlyphs">SCHOOL CARE</text>

  <text class="service" x="875" y="432" font-size="38" textLength="297" lengthAdjust="spacingAndGlyphs">VACATION CARE</text>

  <!-- Phone band -->
  <rect class="phone-band" x="0" y="484" width="1200" height="116" fill="var(--band-blue)"/>
  <text class="headline headline--phone" x="118" y="573" font-size="62" textLength="254" lengthAdjust="spacingAndGlyphs">PHONE:</text>
  <text class="headline headline--phone" x="402" y="573" font-size="100" textLength="648" lengthAdjust="spacingAndGlyphs">07 4000 2318</text>
</svg>
</body>
</html>
```